Brightmere email header for parts

We sell parts to the construction equipment industry. We want a header for our emails that reflect what we do. I will include what we have now but want something for parts only. Added a lot of pictures just so you can look through what we do.

```html
<!DOCTYPE html>
<html lang="en">
<head>
<meta charset="utf-8">
<title>Brightmere – Replacement Parts Email Header</title>
<link rel="stylesheet" href="https://fonts.googleapis.com/css2?family=Bebas+Neue&family=Montserrat:wght@600;700;800&display=swap">
<style>
  :root {
    --page-bg: #d3cfcf;
    --brand-red: #ff0000;
    --ink: #1f1f1f;
    --ink-dark: #231f20;
    --white: #ffffff;
    --part-yellow: #e9b512;
    --part-yellow-deep: #c9940c;
    --part-steel: #3a3a3c;
    --part-grey: #9a9a9c;
  }
  * { margin: 0; padding: 0; box-sizing: border-box; }
  html, body {
    width: 1200px; height: 652px; overflow: hidden;
    background: var(--page-bg);
  }
  .header-banner {
    position: absolute; left: 30px; top: 111px;
    width: 1140px; height: 430px;
    background: var(--white);
    overflow: hidden;
    font-family: "Montserrat", sans-serif;
  }
  .headline-block {
    position: absolute; left: 0; top: 0;
    width: 960px; height: 232px;
    background: var(--brand-red);
  }
  .headline-rule {
    position: absolute; left: 0; top: 232px;
    width: 820px; height: 5px;
    background: var(--ink-dark);
  }
  .headline-title {
    position: absolute; left: 26px; top: 28px;
    font-family: "Bebas Neue", sans-serif;
    font-size: 124px; line-height: 1;
    color: var(--white); letter-spacing: 0.5px;
    white-space: nowrap;
  }
  .headline-sub {
    position: absolute; left: 30px; top: 146px;
    font-weight: 700; font-size: 45px; line-height: 1;
    color: var(--white); white-space: nowrap;
  }
  .brand-name {
    position: absolute; left: 32px; top: 356px;
    display: flex; align-items: center; gap: 10px;
    font-weight: 800; font-size: 30px; color: var(--ink-dark);
    letter-spacing: 0.5px;
  }
  .brand-square {
    width: 22px; height: 22px; background: var(--brand-red);
  }
  .contact-phone {
    position: absolute; left: 294px; top: 268px;
    display: flex; align-items: center; gap: 18px;
    font-weight: 700; font-size: 64px; line-height: 1;
    color: var(--ink-dark); white-space: nowrap;
  }
  .contact-phone svg { width: 52px; height: 52px; }
  .web-bar {
    position: absolute; left: 282px; top: 342px;
    width: 650px; height: 56px;
  }
  .web-bar svg { position: absolute; inset: 0; }
  .web-address {
    position: absolute; left: 36px; top: 10px;
    font-weight: 600; font-size: 33px; line-height: 1;
    color: var(--white); white-space: nowrap;
  }
  .parts-collage {
    position: absolute; left: 0; top: 0;
    width: 1140px; height: 430px;
  }
</style>
</head>
<body>
  <div class="header-banner">
    <div class="headline-block"></div>
    <div class="headline-rule"></div>
    <h1 class="headline-title">REPLACEMENT PARTS</h1>
    <p class="headline-sub">CUSTOM BUILT WATER TANKS</p>

    <div class="web-bar">
      <svg viewBox="0 0 650 56" width="650" height="56">
        <polygon points="14,0 650,0 650,56 0,56" fill="var(--ink-dark)"/>
        <polygon points="8,0 22,0 8,56 -6,56" fill="var(--brand-red)"/>
      </svg>
      <span class="web-address">www.brightmereparts.com</span>
    </div>

    <svg class="parts-collage" viewBox="0 0 1140 430" width="1140" height="430">
      <g fill="var(--ink-dark)">
        <polygon points="1025,-110 1091,-72 1091,4 1025,42 959,4 959,-72"/>
        <polygon points="1160,140 1226,178 1226,254 1160,292 1094,254 1094,178"/>
        <polygon points="1025,390 1091,428 1091,504 1025,542 959,504 959,428"/>
        <polygon points="890,-110 956,-72 956,4 890,42 824,4 824,-72"/>
      </g>
      <polygon role="img" aria-label="Photo of a yellow louvered engine side panel" fill="var(--part-yellow)"
        points="958,14 1024,52 1024,128 958,166 892,128 892,52"/>
      <polygon role="img" aria-label="Photo of a yellow cast steering knuckle on a pallet" fill="var(--part-yellow-deep)"
        points="1093,14 1159,52 1159,128 1093,166 1027,128 1027,52"/>
      <polygon role="img" aria-label="Photo of a black final drive motor with sprocket" fill="var(--part-steel)"
        points="886,140 952,178 952,254 886,292 820,254 820,178"/>
      <polygon role="img" aria-label="Photo of a yellow transmission housing" fill="var(--part-yellow)"
        points="1021,140 1087,178 1087,254 1021,292 955,254 955,178"/>
      <polygon role="img" aria-label="Photo of a black suspension operator seat" fill="var(--part-grey)"
        points="958,266 1024,304 1024,380 958,418 892,380 892,304"/>
      <polygon role="img" aria-label="Photo of a track sprocket and idler wheel" fill="var(--part-steel)"
        points="1093,266 1159,304 1159,380 1093,418 1027,380 1027,304"/>
    </svg>

    <div class="contact-phone">
      <svg viewBox="0 0 24 24" aria-hidden="true">
        <path fill="var(--brand-red)" d="M6.6 10.8a15.2 15.2 0 0 0 6.6 6.6l2.2-2.2c.3-.3.7-.4 1-.2 1.1.4 2.3.6 3.6.6.6 0 1 .4 1 1V20c0 .6-.4 1-1 1A17 17 0 0 1 3 4c0-.6.4-1 1-1h3.5c.6 0 1 .4 1 1 0 1.3.2 2.5.6 3.6.1.3 0 .7-.2 1z"/>
        <path fill="none" stroke="var(--brand-red)" stroke-width="1.8" stroke-linecap="round" d="M14 6.2a4.2 4.2 0 0 1 3.8 3.8M14 2.6a7.8 7.8 0 0 1 7.4 7.4"/>
      </svg>
      <span>555 014 2200</span>
    </div>

    <div class="brand-name">
      <span class="brand-square"></span>
      <span>BRIGHTMERE</span>
    </div>
  </div>
</body>
</html>
```